Business Card Re-Design for a Lighting Designer

I would like my business card re-designed. It is currently high gloss and they scratch too easily. I don not think the current design lends itself well to a matte finish. I have included the current design for reference along with our company logo.
Check out our website for current branding.
http://www.brambleorchidstudio.example

Updates
Some of the top contenders are muslim and it is a holiday for them. I do not want to discriminate and would expect the same courtesy for holidays we celebrate.
Target Market(s)
Interior Designers, Architects
Contact Information for Business Card
Logo - Name, Title, Address, Telephone Number and Extension, Email
Font styles to use
Requirements
Must have
- All the information listed on the current business card. If you use Red, it needs to be the red from our logo.
Nice to have
- Vertical and Horizontal Designs will be entertained.
Should not have
- Requirements for a glossy finish...should not look too corporate since we are a design firm.

```html
<!DOCTYPE html>
<html lang="en">
<head>
<meta charset="utf-8">
<title>Bramble Orchid Studio — Business Card</title>
<link rel="stylesheet" href="https://fonts.googleapis.com/css2?family=Open+Sans:wght@400;600;700&display=swap">
<style>
  :root {
    --brand-red: #9b1b1f;
    --brand-red-soft: #d39a9c;
    --ink: #1b1b1b;
    --ink-muted: #3a3a3a;
    --paper: #ffffff;
    --backdrop: #3b3d40;
    --card-radius: 34px;
  }
  * { box-sizing: border-box; margin: 0; padding: 0; }
  html, body {
    width: 1200px; height: 900px; overflow: hidden;
    background: var(--backdrop);
    font-family: "Open Sans", sans-serif;
  }
  .sheet {
    width: 1200px; height: 900px;
    display: flex; flex-direction: column; align-items: center; justify-content: center;
    gap: 56px;
  }
  .card {
    position: relative;
    width: 630px; height: 360px;
    border-radius: var(--card-radius);
    overflow: hidden;
  }
  /* Back side */
  .card--back {
    background: var(--brand-red);
    display: flex; align-items: center; justify-content: center;
  }
  .brand {
    display: flex; align-items: center; gap: 16px;
    font-weight: 600; letter-spacing: 0.04em;
  }
  .brand__square { width: 34px; height: 34px; flex: none; }
  .card--back .brand { color: var(--paper); font-size: 30px; }
  .card--back .brand__square { background: var(--paper); }

  /* Front side */
  .card--front { background: var(--paper); }
  .card__band {
    position: absolute; left: 0; right: 0; bottom: 0; height: 16px;
    background: var(--brand-red);
  }
  .card--front .brand {
    position: absolute; right: 40px; top: 92px;
    color: var(--ink); font-size: 25px;
  }
  .card--front .brand__square { background: var(--brand-red); width: 30px; height: 30px; }
  .brand-rule {
    position: absolute; right: 40px; top: 150px;
    width: 300px; height: 4px; background: var(--brand-red-soft);
  }
  .person { position: absolute; left: 44px; top: 150px; }
  .person__name { color: var(--brand-red); font-weight: 700; font-size: 30px; line-height: 1.1; }
  .person__title { color: var(--ink); font-weight: 700; font-size: 15px; margin-top: 6px; margin-left: 4px; }
  .address {
    position: absolute; left: 48px; top: 232px;
    color: var(--ink-muted); font-size: 13px; line-height: 1.45;
  }
  .contact-list {
    position: absolute; left: 48px; top: 278px;
    list-style: none; color: var(--ink-muted); font-size: 13px; line-height: 1.6;
  }
  .contact-list li { display: flex; align-items: center; gap: 10px; }
  .contact-list svg { width: 13px; height: 13px; flex: none; fill: var(--brand-red); }
</style>
</head>
<body>
<main class="sheet">
  <section class="card card--back" aria-label="Card back">
    <div class="brand">
      <span class="brand__square"></span>
      <span class="brand__name">Bramble Orchid Studio</span>
    </div>
  </section>

  <section class="card card--front" aria-label="Card front">
    <div class="brand">
      <span class="brand__square"></span>
      <span class="brand__name">Bramble Orchid Studio</span>
    </div>
    <div class="brand-rule"></div>

    <div class="person">
      <p class="person__name">Marlo Fenwick</p>
      <p class="person__title">Principal</p>
    </div>

    <address class="address" style="font-style:normal">
      Larkspur Commons Way Suite 13<br>
      Fairhaven, Oregon 97001 USA
    </address>

    <ul class="contact-list">
      <li>
        <svg viewBox="0 0 24 24" aria-hidden="true"><path d="M6.6 10.8a15.1 15.1 0 0 0 6.6 6.6l2.2-2.2a1 1 0 0 1 1-.25 11.4 11.4 0 0 0 3.6.57 1 1 0 0 1 1 1V20a1 1 0 0 1-1 1A17 17 0 0 1 3 4a1 1 0 0 1 1-1h3.5a1 1 0 0 1 1 1c0 1.25.2 2.45.57 3.57a1 1 0 0 1-.25 1z"/></svg>
        <span>555.014.2290 x1</span>
      </li>
      <li>
        <svg viewBox="0 0 24 24" aria-hidden="true"><path d="M2 5h20v14H2zm2 2v.4l8 5.2 8-5.2V7zm0 2.8V17h16V9.8l-8 5.2z"/></svg>
        <span>any@brambleorchidstudio.example</span>
      </li>
      <li>
        <svg viewBox="0 0 24 24" aria-hidden="true"><path d="M12 2a10 10 0 1 0 0 20 10 10 0 0 0 0-20zm6.9 6h-3a15 15 0 0 0-1.3-4A8 8 0 0 1 18.9 8zM12 4c.8 1.1 1.5 2.5 1.9 4h-3.8c.4-1.5 1.1-2.9 1.9-4zM4.3 14a8 8 0 0 1 0-4h3.4a16 16 0 0 0 0 4zm.8 2h3a15 15 0 0 0 1.3 4A8 8 0 0 1 5.1 16zm3-8h-3a8 8 0 0 1 4.3-4 15 15 0 0 0-1.3 4zM12 20c-.8-1.1-1.5-2.5-1.9-4h3.8c-.4 1.5-1.1 2.9-1.9 4zm2.3-6H9.7a14 14 0 0 1 0-4h4.6a14 14 0 0 1 0 4zm.3 6a15 15 0 0 0 1.3-4h3a8 8 0 0 1-4.3 4zm1.7-6a16 16 0 0 0 0-4h3.4a8 8 0 0 1 0 4z"/></svg>
        <span>www.brambleorchidstudio.example</span>
      </li>
    </ul>

    <div class="card__band"></div>
  </section>
</main>
</body>
</html>
```